Business card for communications

Need a business card for my consulting business - I work with not for profits, start ups and social enterprises on their media, communications campaigns.

Please see my website for colours, images and fonts www.morelbratton.example

Dana Morelbrat
Communications & Campaign strategist
Sydney - Melbourne
M: 0498 317 026
E: dana@morelbratton.example
S: danamorelbrat
W: morelbratton.example
T: @danamorelbrat

(above is info only and can be presented any way e.g. should not have to be M for mobile - it should be an icon)
Updates

Dear designers I have updated the brief and uploaded high res images from my website for you to use. The designs so far with the use of images and icons are much better so far. Thank you I look forward to receiving your revised designs. Dana Morelbrat

Industry/Entity Type

Communications

Font styles to use
Sans Serif

Requirements
Must have
• Icons for contact details
Images from the website www.morelbratton.example
Nice to have
• Images - attached

```html
<!DOCTYPE html>
<html lang="en">
<head>
<meta charset="utf-8">
<title>Dana Morelbrat – Business Card</title>
<link href="https://fonts.googleapis.com/css2?family=Abel&family=Open+Sans:wght@400;600&display=swap" rel="stylesheet">
<style>
  :root {
    --bg: #e9e6e1;
    --yellow: #f6dc0c;
    --yellow-deep: #e9cc00;
    --ink: #2b2b2b;
    --ink-soft: #3d3d3a;
    --frame: #ffffff;
    --desk-a: #c9a06a;
    --desk-b: #e8e4dc;
    --portrait-light: #f1ece8;
    --portrait-mid: #d9cbc3;
  }
  * { box-sizing: border-box; margin: 0; padding: 0; }
  html, body { width: 1200px; height: 1023px; overflow: hidden; }
  body {
    background: var(--bg);
    font-family: "Open Sans", Arial, sans-serif;
    color: var(--ink);
    position: relative;
  }
  .card {
    position: absolute;
    left: 240px;
    width: 720px;
    height: 411px;
    background: linear-gradient(160deg, var(--yellow) 0%, var(--yellow-deep) 100%);
    box-shadow: 0 6px 18px rgba(0,0,0,.18);
    overflow: hidden;
  }
  .card--front { top: 70px; }
  .card--back { top: 542px; }

  /* Front */
  .front-name {
    position: absolute; left: 32px; top: 26px;
    font-family: "Abel", "Open Sans", sans-serif;
    font-weight: 400;
    font-size: 44px; letter-spacing: 1.5px; color: var(--ink);
    line-height: 1;
  }
  .front-title {
    position: absolute; left: 34px; top: 80px;
    font-size: 13px; letter-spacing: .6px; text-transform: uppercase; color: var(--ink-soft);
  }
  .desk-photo {
    position: absolute; left: 240px; top: 108px; width: 480px; height: 170px;
    background: linear-gradient(120deg, var(--desk-a) 0%, #d9b785 45%, var(--desk-b) 100%);
  }
  .portrait-inset {
    position: absolute; left: 30px; top: 176px; width: 196px; height: 200px;
    background: var(--frame); padding: 8px;
    box-shadow: 0 2px 6px rgba(0,0,0,.2);
  }
  .portrait-inset .photo {
    width: 100%; height: 100%;
    background: linear-gradient(135deg, var(--portrait-light) 0%, var(--portrait-mid) 100%);
  }
  .contacts {
    position: absolute; top: 296px;
    list-style: none; font-size: 14px; color: var(--ink);
  }
  .contacts--primary { left: 256px; }
  .contacts--social { left: 500px; }
  .contacts li { display: flex; align-items: center; gap: 9px; height: 28px; white-space: nowrap; }
  .icon { width: 16px; height: 16px; flex: none; }

  /* Back */
  .portrait-large {
    position: absolute; left: 0; top: 0; width: 380px; height: 411px;
    background: linear-gradient(135deg, var(--portrait-light) 0%, var(--portrait-mid) 100%);
  }
  .back-text {
    position: absolute; right: 36px; top: 190px; text-align: right;
  }
  .back-name {
    font-family: "Abel", "Open Sans", sans-serif;
    font-weight: 400;
    font-size: 40px; letter-spacing: 1.5px; line-height: 1; margin-bottom: 18px;
  }
  .services { list-style: none; font-size: 13px; text-transform: uppercase; letter-spacing: .5px; color: var(--ink-soft); }
  .services li { line-height: 21px; }
  .services li::after { content: " •"; color: var(--ink); }
</style>
</head>
<body>

<section class="card card--front">
  <h1 class="front-name">DANA MORELBRAT</h1>
  <p class="front-title">Communications &amp; Campaign Strategist</p>

  <div class="desk-photo" role="img" aria-label="Overhead photo of a work desk with a laptop, papers and hands typing"></div>

  <div class="portrait-inset">
    <div class="photo" role="img" aria-label="Portrait photo of Dana Morelbrat"></div>
  </div>

  <ul class="contacts contacts--primary">
    <li>
      <svg class="icon" viewBox="0 0 16 16"><rect width="16" height="16" rx="2" fill="#2b2b2b"/><rect x="5" y="3" width="6" height="10" rx="1" fill="none" stroke="#f6dc0c" stroke-width="1.3"/></svg>
      0498 317 026
    </li>
    <li>
      <svg class="icon" viewBox="0 0 16 16"><rect width="16" height="16" rx="2" fill="#2b2b2b"/><rect x="3" y="5" width="10" height="7" fill="none" stroke="#f6dc0c" stroke-width="1.2"/><path d="M3 5l5 4 5-4" fill="none" stroke="#f6dc0c" stroke-width="1.2"/></svg>
      dana@morelbratton.example
    </li>
    <li>
      <svg class="icon" viewBox="0 0 16 16"><rect width="16" height="16" rx="2" fill="#2b2b2b"/><path d="M8 13s-3.5-4-3.5-6.5a3.5 3.5 0 0 1 7 0C11.5 9 8 13 8 13z" fill="#f6dc0c"/><circle cx="8" cy="6.5" r="1.2" fill="#2b2b2b"/></svg>
      Sydney - Melbourne
    </li>
  </ul>

  <ul class="contacts contacts--social">
    <li>
      <svg class="icon" viewBox="0 0 16 16"><rect width="16" height="16" rx="2" fill="#2b2b2b"/><path d="M3.5 4.5h9v5.5h-5l-2.5 2.2v-2.2h-1.5z" fill="none" stroke="#f6dc0c" stroke-width="1.2" stroke-linejoin="round"/></svg>
      danamorelbrat
    </li>
    <li>
      <svg class="icon" viewBox="0 0 16 16"><rect width="16" height="16" rx="2" fill="#2b2b2b"/><circle cx="8" cy="8" r="1.8" fill="none" stroke="#f6dc0c" stroke-width="1.2"/><path d="M9.8 6.5v2.3c0 1 1.7 1 1.7-.6a3.6 3.6 0 1 0-1.4 2.8" fill="none" stroke="#f6dc0c" stroke-width="1.2" stroke-linecap="round"/></svg>
      @danamorelbrat
    </li>
    <li>
      <svg class="icon" viewBox="0 0 16 16"><rect width="16" height="16" rx="2" fill="#2b2b2b"/><circle cx="8" cy="8" r="4.5" fill="none" stroke="#f6dc0c" stroke-width="1.2"/><path d="M3.5 8h9M8 3.5v9" stroke="#f6dc0c" stroke-width="1"/></svg>
      morelbratton.example
    </li>
  </ul>
</section>

<section class="card card--back">
  <div class="portrait-large" role="img" aria-label="Portrait photo of Dana Morelbrat"></div>
  <div class="back-text">
    <h2 class="back-name">DANA MORELBRAT</h2>
    <ul class="services">
      <li>Communications Strategy</li>
      <li>Media Relations</li>
      <li>PR &amp; Campaigns</li>
      <li>Strategic Counsel</li>
    </ul>
  </div>
</section>

</body>
</html>
```